RD'S

This is for a NY state legal cannabis gummy brand called Sunny Chews. It's airplane themed but we can not have cartoons or animals on the bag like our original bag.
The company is RD's. The processor we are working with is called Velvet Farm.

The current logo for RD's can not be used since it has a cat. The letters must be the logo. For the original bags we used, one of the pictures is included of the green bag.

Velvet Farm logo must be on the bag like such:
"Powered by" and the logo.
Preferably on the back of the bag.

There are 3 SKUs:

Silver Cherry (Sleep)
100mg THC, 100mg CBN and 100mg CBD and is Nano Infused (15 minute onset)

Green Hills Lime Zing (Focus)
Contains 100mg THC 100mg, 50mg CBG and 50mg CBD and is Nano Infused (15 minute onset)

Bright Mango - (Take Off)
100mg THC and 100mg THCV and is Nano Infused (15 minute onset)

Ingredients for all are:

Organic Tapioca Syrup, Organic Cane Sugar, Water, Beef Gelatin, Natural Flavor, Citric Acid, Nano Emuslified Cannabis Extract, Hemp extract, Fruit and vegetable juice for color and Ascorbic Acid

Bag size is 5.5" Tall, 3.5" wide and 1.5" gusset

Need a 2"x1" empty space on the back towards the bottom for a compliance sticker we will add

Bag must be NY state compliant. The rules are in the Pdf file i uploaded

Pick 1 from the 2 files for NY state warning, uploaded below
- Must have any one of the following three universal symbols at a minimum size of 1.25
inch in height for the square symbol, 0.5 inch in width for the vertical symbol, and
0.5 inch in height for the horizontal symbol. The symbol and its colors cannot be
altered

Must have this warning on the back in 6pt font:

WARNING: This product contains cannabis and THC. KEEP OUT OF REACH OF CHILDREN AND PETS. For use only by persons 21 years and older. Do NOT consume or use if pregnant or nursing. Cannabis can impair concentration and coordination. Do not operate a vehicle or machinery under the influence of cannabis. In case of accidental ingestion or overconsumption, contact the Poison Center at 1-800-555-0187. Effects of this product may be delayed by 4 or more hours.

```html
<!DOCTYPE html>
<html lang="en">
<head>
<meta charset="utf-8">
<title>RD's Sunny Chews – Pouch Front and Back</title>
<link href="https://fonts.googleapis.com/css2?family=Montserrat:wght@500;900&family=Oswald:wght@400;500;600&family=PT+Sans+Narrow:wght@400;700&display=swap" rel="stylesheet">
<style>
  :root{
    --page:#eceff2;
    --sky-top:#2a5fe6;
    --sky-mid:#1aa8f2;
    --sky-glow:#2fd3f2;
    --purple:#3d20a3;
    --purple-deep:#2e168a;
    --cyan:#1ec6ea;
    --ink:#141026;
    --white:#ffffff;
  }
  *{box-sizing:border-box;margin:0;padding:0}
  html,body{width:1200px;height:831px;overflow:hidden;background:var(--page)}
  .canvas{position:relative;width:1200px;height:831px}
  .pouch{position:absolute;top:71px;width:480px;height:697px;background:var(--purple);border-radius:10px 10px 4px 4px;overflow:hidden;color:var(--white)}
  .pouch--front{left:101px}
  .pouch--back{left:605px}
  .pouch > *{position:absolute}

  .scene-art{left:0;top:0;width:100%}
  .pouch--front .scene-art{height:450px;background:linear-gradient(180deg,var(--sky-top) 0%,var(--sky-mid) 38%,var(--sky-glow) 62%,#5b3cc4 82%,var(--purple) 100%)}
  .pouch--back .scene-art{height:250px;background:linear-gradient(180deg,var(--sky-top) 0%,var(--sky-mid) 30%,var(--sky-glow) 48%,#4f30bd 72%,var(--purple) 100%)}

  .child-warning{top:22px;left:0;width:100%;text-align:center;font:500 11px/1 'Oswald',sans-serif;letter-spacing:4.2px}

  .brand-mark{left:0;width:100%;text-align:center;font-family:'Montserrat',sans-serif;font-weight:900;color:var(--ink);letter-spacing:-3px}
  .pouch--front .brand-mark{top:78px;font-size:82px;line-height:1}
  .pouch--back .brand-mark{top:206px;font-size:44px;line-height:1;letter-spacing:-2px}

  .product-name{font-family:'Montserrat',sans-serif;font-weight:900;line-height:1}
  .product-name .accent{color:var(--cyan)}
  .pouch--front .product-name{left:96px;top:414px;font-size:64px;letter-spacing:2px}
  .pouch--front .product-name span{display:block;margin-bottom:6px}
  .pouch--back .product-name{left:0;width:100%;text-align:center;top:262px;font-size:40px;letter-spacing:3px}

  .effect-tag{left:99px;top:549px;width:90px;height:41px;background:var(--cyan);color:var(--ink);font:600 27px/41px 'Oswald',sans-serif;text-align:center}
  .flavor-rule{left:189px;top:549px;width:194px;height:2px;background:var(--cyan)}
  .flavor-front{left:200px;top:556px;font:400 19.5px/1.6 'Oswald',sans-serif;color:var(--cyan);letter-spacing:.3px;white-space:nowrap}
  .potency-rule{left:189px;top:590px;width:112px;height:2px;background:var(--cyan)}
  .potency-divider{left:301px;top:590px;width:2px;height:59px;background:var(--cyan)}
  .potency{left:99px;top:600px;width:196px;font:500 11px/14.5px 'Montserrat',sans-serif}

  .processor{width:78px;text-align:center}
  .pouch--front .processor{left:315px;top:592px}
  .pouch--back .processor{left:338px;top:526px}
  .processor__label{font:500 8px/1 'Oswald',sans-serif;letter-spacing:2px;display:block;margin-bottom:5px}
  .processor__name{display:flex;align-items:center;justify-content:center;gap:4px;font:500 13px/1 'Oswald',sans-serif;white-space:nowrap}
  .processor__dot{width:8px;height:8px;border-radius:50%;background:var(--white);flex:none}

  .category-band{left:0;top:649px;width:100%;height:28px;background:var(--cyan);text-align:center;font:500 13px/28px 'Oswald',sans-serif;letter-spacing:4px}

  .copy{left:61px;top:307px;width:170px;font:400 8px/9.8px 'PT Sans Narrow',sans-serif}
  .copy h3{color:var(--cyan);font:700 8.4px/1 'PT Sans Narrow',sans-serif;margin-bottom:2px}
  .copy p{margin-bottom:8px}

  .storage{left:61px;top:484px;width:66px;font:500 11px/14px 'Oswald',sans-serif;color:var(--cyan);text-transform:uppercase;white-space:nowrap;letter-spacing:-.2px}
  .symbols{left:133px;top:484px;display:flex;height:30px}
  .symbols div{width:31px;height:30px;background:var(--white);display:flex;align-items:center;justify-content:center}
  .symbols .symbol-dark{background:#111}

  .nutrition{left:243px;top:307px;width:174px;height:206px;background:var(--white);border:2px solid var(--cyan);color:#111;padding:3px 5px;font:400 7px/1.25 'PT Sans Narrow',sans-serif}
  .nutrition h3{font:600 17px/1 'Oswald',sans-serif;border-bottom:1px solid #111;padding-bottom:2px}
  .nutrition .row{display:flex;justify-content:space-between;border-bottom:1px solid #111;padding:2px 0}
  .nutrition .thick{border-bottom:4px solid #111}
  .nutrition .mid{border-bottom:2.5px solid #111}
  .nutrition .cal{font:700 9px/1 'PT Sans Narrow',sans-serif}
  .nutrition .indent{padding-left:10px}
  .nutrition .indent2{padding-left:18px}
  .nutrition b{font-weight:700}
  .nutrition .foot{position:absolute;left:5px;right:5px;bottom:4px;border-top:2.5px solid #111;padding-top:6px;font-size:5.5px}

  .sticker-area{left:66px;top:522px;width:261px;height:124px;border:1px solid var(--white)}

  .flavor-rule-back{left:343px;top:600px;width:74px;height:2px;background:var(--cyan)}
  .flavor-back{left:343px;top:604px;font:400 19px/21px 'Oswald',sans-serif;white-space:nowrap}
  .flavor-back .accent{color:var(--cyan)}
</style>
</head>
<body>
<main class="canvas">

  <section class="pouch pouch--front" aria-label="Pouch front">
    <div class="scene-art" role="img" aria-label="Night sky illustration with an airliner leaving a cloud trail above a purple city skyline with a suspension bridge"></div>
    <p class="child-warning">KEEP AWAY FROM CHILDREN AND PETS</p>
    <h1 class="brand-mark">RD's</h1>
    <h2 class="product-name"><span>SUNNY</span><span class="accent">CHEWS</span></h2>
    <div class="effect-tag">FOCUS</div>
    <div class="flavor-rule"></div>
    <p class="flavor-front">GREEN HILLS LIME ZING</p>
    <div class="potency-rule"></div>
    <div class="potency-divider"></div>
    <p class="potency">Contains 100mg THC 100mg, 50mg CBG and 50mg CBD and is Nano Infused (15 minute onset)</p>
    <div class="processor">
      <span class="processor__label">POWERED BY</span>
      <span class="processor__name"><i class="processor__dot"></i>Velvet Farm</span>
    </div>
    <p class="category-band">CANNABIS INFUSED GUMMIES WITH CBN</p>
  </section>

  <section class="pouch pouch--back" aria-label="Pouch back">
    <div class="scene-art" role="img" aria-label="City skyline illustration with a suspension bridge and harbour statue against a glowing sky"></div>
    <p class="child-warning">KEEP AWAY FROM CHILDREN AND PETS</p>
    <h1 class="brand-mark">RD's</h1>
    <h2 class="product-name">SUNNY <span class="accent">CHEWS</span></h2>

    <div class="copy">
      <h3>INGREDIENTS:</h3>
      <p>Organic Tapioca Syrup, Organic Cane Sugar, Water, Beef Gelatin, Natural Flavor, Citric Acid, Nano Emulsified Cannabis Extract, Hemp extract, Fruit and vegetable juice for color and Ascorbic Acid</p>
      <h3>WARNING:</h3>
      <p>This product contains cannabis and THC. KEEP OUT OF REACH OF CHILDREN AND PETS. For use only by persons 21 years and older. Do NOT consume or use if pregnant or nursing. Cannabis can impair concentration and coordination. Do not operate a vehicle or machinery under the influence of cannabis. In case of accidental ingestion or overconsumption, contact the Poison Center at 1-800-555-0187. Effects of this product may be delayed by 4 or more hours.</p>
    </div>

    <p class="storage">Store in cool<br>dry place</p>
    <div class="symbols" aria-label="Compliance symbols">
      <div><svg width="22" height="20" viewBox="0 0 22 20"><polygon points="11,1 21,19 1,19" fill="#f7d21a" stroke="#111" stroke-width="1.5"/></svg></div>
      <div><svg width="22" height="22" viewBox="0 0 22 22"><circle cx="11" cy="11" r="9" fill="#fff" stroke="#d6202a" stroke-width="2.5"/></svg></div>
      <div class="symbol-dark"></div>
    </div>

    <div class="nutrition">
      <h3>Nutrition Facts</h3>
      <div class="row" style="border:0;display:block">Serving Size: 1 Gummy (1 piece)<br>Servings Per Container: 10</div>
      <div class="row thick"></div>
      <div class="row"><b>Amount Per Serving</b></div>
      <div class="row mid cal"><span>Calories 10</span></div>
      <div class="row" style="justify-content:flex-end"><b>% Daily Value*</b></div>
      <div class="row"><span><b>Total Carbohydrate</b> 2g</span><b>1%</b></div>
      <div class="row indent"><span>Total Sugars 2g</span></div>
      <div class="row indent2"><span>Includes 2g Added Sugars <b>4%</b></span></div>
      <div class="row mid"><span><b>Sodium</b> 2mg</span><b>0%</b></div>
      <div class="foot"><b>*Daily Value not established.</b></div>
    </div>

    <div class="sticker-area" aria-label="Reserved space for compliance sticker"></div>

    <div class="processor">
      <span class="processor__label">POWERED BY</span>
      <span class="processor__name"><i class="processor__dot"></i>Velvet Farm</span>
    </div>
    <div class="flavor-rule-back"></div>
    <p class="flavor-back"><span class="accent">GREEN HILLS</span><br>LIME ZING</p>

    <p class="category-band">CANNABIS INFUSED GUMMIES WITH CBN</p>
  </section>

</main>
</body>
</html>
```